Fruits and Vegetables distribution company needs a new eye catching website

We need to get our website up to date. Our clients will look at our website to learn about our products and services. Our design needs to be simple yet impactful to make our brand memorable to our visitors. We need to have somewhere to tell our clients about our history, products and services, our team. We can throw in a few fun facts and figures and maybe some testimonials to impress. We have 4 theme colors that we want to incorporate into the design, you can get in touch for the HEX/RGB codes. Please remember that smooth operation of any animations and interactions is very important.

Need extra days to review

```html
<!DOCTYPE html>
<html lang="en">
<head>
<meta charset="utf-8">
<title>Harvest Lane — Fruits &amp; Vegetables Distribution</title>
<link rel="stylesheet" href="https://fonts.googleapis.com/css2?family=Open+Sans:ital,wght@0,400;0,600;0,700;1,400&family=Tinos:wght@400;700&display=swap">
<style>
:root{
  --red:#c0161e;
  --orange:#f6a10c;
  --green:#6dbb2c;
  --green-light:#9fd35a;
  --dark:#262626;
  --darker:#1b1b1b;
  --text:#444;
  --muted:#8a8a8a;
  --white:#fff;
}
*{margin:0;padding:0;box-sizing:border-box}
html,body{width:1200px;height:3651px;overflow:hidden;background:#fff}
body{font-family:"Open Sans",Arial,sans-serif;color:var(--text)}
.page{position:relative;width:1200px;height:3651px;overflow:hidden;background:#fff}
.abs{position:absolute}
.serif{font-family:"Tinos","Times New Roman",serif}

/* header */
.site-header{position:absolute;left:0;top:0;width:1200px;height:102px;background:#fff;z-index:5;box-shadow:0 2px 6px rgba(0,0,0,.08)}
.brand{position:absolute;left:168px;top:30px;display:flex;align-items:center;gap:12px}
.brand-dot{width:40px;height:40px;border-radius:50%;background:var(--red)}
.brand-name{font-family:"Tinos",serif;font-size:34px;color:var(--dark);letter-spacing:1px}
.main-nav{position:absolute;right:180px;top:42px;display:flex;gap:28px;font-size:15px;font-weight:600;color:#333;letter-spacing:.3px}

/* hero */
.hero{position:absolute;left:0;top:102px;width:1200px;height:620px;
  background:radial-gradient(ellipse at 30% 60%,#c4331c 0%,transparent 45%),radial-gradient(ellipse at 75% 40%,#7a1d2a 0%,transparent 40%),radial-gradient(ellipse at 50% 20%,#4f7d2a 0%,transparent 55%),linear-gradient(180deg,#3c5a22,#6b2a1a 60%,#8b3a1c)}
.hero-title{position:absolute;left:0;width:1200px;top:182px;text-align:center;color:#fff;font-family:"Tinos",serif;font-size:58px;letter-spacing:1px;line-height:1}
.hero-sub{position:absolute;left:0;width:1200px;top:256px;text-align:center;color:#fff;font-family:"Tinos",serif;font-size:40px;letter-spacing:1px;line-height:1}
.hero-down{position:absolute;left:576px;top:324px;width:48px;height:48px;border-radius:50%;background:var(--red)}
.section-badge{position:absolute;width:60px;height:60px;border-radius:50%;background:#fff;box-shadow:0 2px 6px rgba(0,0,0,.15);display:flex;align-items:center;justify-content:center}
.section-badge span{width:24px;height:24px;border-radius:50%;background:var(--red)}

/* headings */
.section-title{position:absolute;left:0;width:1200px;text-align:center;font-family:"Tinos",serif;font-size:36px;color:var(--red);letter-spacing:1px}

/* history */
.history-bg{position:absolute;left:0;top:720px;width:1200px;height:340px;background:linear-gradient(180deg,#fff 0%,#eef0f0 40%,#fff 100%)}
.history-text{position:absolute;left:180px;width:840px;top:832px;text-align:center;font-size:20px;line-height:31px;color:#444}
.btn-orange{position:absolute;left:512px;top:950px;width:154px;height:40px;background:var(--orange);color:#fff;font-size:14px;font-weight:700;display:flex;align-items:center;justify-content:center;border-radius:3px}
.crate-img{position:absolute;left:336px;top:1030px;width:496px;height:282px;border-radius:40% 40% 45% 45%/30% 30% 60% 60%;background:radial-gradient(ellipse at 50% 30%,#d2432a,#8a5a30 55%,#5d7e2c 80%,transparent 82%)}

/* products */
.hills{position:absolute;left:0;top:1500px;width:1200px;height:420px;background:linear-gradient(180deg,#fff 0%,#dfe9d9 35%,#7fa65a 70%,#4f7e2e 100%)}
.product-card{position:absolute;top:1429px;width:254px;height:324px;background:#fff;border:1px solid #ddd;box-shadow:0 3px 10px rgba(0,0,0,.12);text-align:center}
.product-img{position:absolute;left:32px;top:28px;width:190px;height:110px;border-radius:50%}
.product-title{position:absolute;left:0;width:100%;top:196px;font-size:17px;font-weight:600;color:#333}
.product-desc{position:absolute;left:24px;width:206px;top:226px;font-size:13px;line-height:18px;color:var(--muted)}
.product-more{position:absolute;left:112px;top:270px;width:30px;height:30px;border-radius:50%;background:var(--orange)}
.arrow{position:absolute;width:26px;height:56px}

/* testimonials */
.testi-title{position:absolute;left:0;width:1200px;text-align:center;font-family:"Tinos",serif;font-size:32px;color:#fff;letter-spacing:1px}
.testi-card{position:absolute;top:2035px;width:256px;height:160px;background:#fff;border-radius:3px;box-shadow:0 2px 8px rgba(0,0,0,.12)}
.quote-mark{position:absolute;left:20px;top:22px;font-family:"Tinos",serif;font-size:46px;color:var(--orange);line-height:1}
.testi-text{position:absolute;left:50px;width:186px;top:30px;font-size:11.5px;font-style:italic;line-height:21px;color:#777}
.author{position:absolute;top:2208px;display:flex;align-items:center;gap:10px}
.author-photo{width:42px;height:42px;border-radius:50%;background:linear-gradient(135deg,#a48d7a,#5c4a3e)}
.author-name{font-size:12px;font-weight:700;color:#fff;line-height:17px}
.author-loc{font-size:11px;color:#fff;line-height:15px}

/* team */
.team-title{position:absolute;left:0;width:1200px;top:2364px;text-align:center;font-family:"Tinos",serif;font-size:32px;color:#333;letter-spacing:1px}
.team-card{position:absolute;top:2424px;width:192px;height:290px;background:#fff;border:1px solid #ddd;box-shadow:0 2px 8px rgba(0,0,0,.1);text-align:center}
.team-photo{position:absolute;left:0;top:0;width:100%;height:144px;background:linear-gradient(180deg,#c8cbcd,#8f8a86)}
.member-name{position:absolute;left:0;width:100%;top:160px;font-size:14px;color:var(--green)}
.member-bio{position:absolute;left:14px;width:164px;top:182px;font-size:10.5px;line-height:14px;color:#555}
.member-social{position:absolute;left:0;width:100%;top:240px;display:flex;justify-content:center;gap:13px}
.member-social i{width:10px;height:10px;background:#333;border-radius:2px}
.btn-red{position:absolute;left:46px;top:264px;width:98px;height:22px;background:var(--red);color:#fff;font-size:9.5px;font-weight:700;display:flex;align-items:center;justify-content:center;border-radius:2px}

/* fun facts */
.facts-title{position:absolute;left:208px;top:2912px;font-family:"Tinos",serif;font-size:32px;color:#fff;letter-spacing:1px}
.fact{position:absolute;left:204px;width:480px;display:flex;gap:14px;color:#fff;font-size:14.5px;line-height:24px}
.fact-icon{flex:none;width:18px;height:20px;margin-top:3px;border:2px solid #fff;border-radius:50% 50% 45% 45%}
.basket-img{position:absolute;left:700px;top:2884px;width:322px;height:306px;border-radius:48%;background:radial-gradient(circle at 45% 35%,#e4484a,#b21d2c 45%,#8c5a2c 75%,transparent 77%)}

/* footer */
.footer-logo{position:absolute;left:182px;top:3320px;width:160px;text-align:center;color:#bdbdbd}
.footer-logo .mark{width:48px;height:48px;border-radius:50%;border:2px solid #bdbdbd;margin:0 auto 16px}
.footer-logo .name{font-family:"Tinos",serif;font-size:26px;letter-spacing:1px}
.foot-col{position:absolute;top:3320px;color:#ccc}
.foot-col h4{font-family:"Tinos",serif;font-weight:400;font-size:17px;letter-spacing:1px;color:#e0e0e0;margin-bottom:16px}
.foot-col li{list-style:none;font-size:12.5px;line-height:27px}
.contact-row{display:flex;align-items:center;gap:8px;font-size:12.5px;line-height:28px}
.social{display:flex;gap:9px;margin-top:8px}
.social i{width:28px;height:28px;border:1.5px solid #ddd;border-radius:50%}
.copyright{position:absolute;left:0;top:3578px;width:1200px;height:73px;background:var(--darker);color:#aaa;font-size:12px;display:flex;align-items:center;justify-content:center}
</style>
</head>
<body>
<div class="page">

  <!-- hero -->
  <section class="hero" role="img" aria-label="Photo of fresh vegetables and fruits: peppers, tomatoes, carrots, greens and beets"></section>
  <h1 class="hero-title">FRUITS &amp; VEGETABLES</h1>
  <p class="hero-sub">DISTRIBUTION SERVICES</p>
  <div class="hero-down">
    <svg width="48" height="48" viewBox="0 0 48 48"><path d="M15 20l9 9 9-9" fill="none" stroke="#fff" stroke-width="4" stroke-linecap="round" stroke-linejoin="round"/></svg>
  </div>
  <svg class="abs" style="left:0;top:640px" width="1200" height="90" viewBox="0 0 1200 90"><path d="M0 90 L0 60 Q600 -10 1200 60 L1200 90 Z" fill="#fff"/></svg>

  <header class="site-header">
    <div class="brand"><span class="brand-dot"></span><span class="brand-name">Harvest Lane</span></div>
    <nav class="main-nav"><span>ABOUT US</span><span>PRODUCTS</span><span>SERVICES</span><span>TESTIMONIAL</span><span>FACTS</span><span>CONTACT</span></nav>
  </header>

  <!-- history -->
  <div class="history-bg"></div>
  <div class="section-badge" style="left:558px;top:656px"><span></span></div>
  <h2 class="section-title" style="top:768px">OUR HISTORY</h2>
  <p class="history-text">In massa libero interdum nec interdum vel blandit sed nulla In ullamcorper est eget tempor cursus neque Morbi porta libero id ullamcorper nonummy nibh ligula pulvinar metus eget consectetuer augue nisi</p>
  <div class="btn-orange">READ MORE</div>
  <div class="crate-img" role="img" aria-label="Wooden crate filled with vegetables and fruit"></div>

  <!-- products -->
  <div class="hills" role="img" aria-label="Green terraced hills landscape"></div>
  <h2 class="section-title" style="top:1350px">PRODUCTS &amp; SERVICES</h2>
  <svg class="arrow" style="left:130px;top:1560px" viewBox="0 0 26 56"><path d="M22 4L4 28l18 24" fill="none" stroke="#444" stroke-width="3"/></svg>
  <svg class="arrow" style="left:1060px;top:1560px" viewBox="0 0 26 56"><path d="M4 4l18 24L4 52" fill="none" stroke="#444" stroke-width="3"/></svg>

  <article class="product-card" style="left:185px">
    <div class="product-img" role="img" aria-label="Assorted peppers and tomatoes" style="background:radial-gradient(ellipse,#e0441c,#f29a1a 60%,transparent 72%)"></div>
    <h3 class="product-title">PRODUCT TITLE</h3>
    <p class="product-desc">Alibero id ullamcorper nonummy nibh ligula pulvinar metus</p>
    <div class="product-more"></div>
  </article>
  <article class="product-card" style="left:462px">
    <div class="product-img" role="img" aria-label="Basket of mixed vegetables" style="background:radial-gradient(ellipse,#6aa830,#b5402a 55%,transparent 72%)"></div>
    <h3 class="product-title">PRODUCT TITLE</h3>
    <p class="product-desc">Alibero id ullamcorper nonummy nibh ligula pulvinar metus</p>
    <div class="product-more"></div>
  </article>
  <article class="product-card" style="left:750px">
    <div class="product-img" role="img" aria-label="Pile of assorted fresh fruit" style="background:radial-gradient(ellipse,#f0a020,#c2302a 50%,#5e9a2a 65%,transparent 72%)"></div>
    <h3 class="product-title">PRODUCT TITLE</h3>
    <p class="product-desc">Alibero id ullamcorper nonummy nibh ligula pulvinar metus</p>
    <div class="product-more"></div>
  </article>

  <!-- testimonials -->
  <svg class="abs" style="left:0;top:1860px" width="1200" height="520" viewBox="0 0 1200 520" preserveAspectRatio="none">
    <path d="M0 30 Q600 -20 1200 30 L1200 470 Q600 360 0 470 Z" fill="var(--orange)"/>
  </svg>
  <div class="section-badge" style="left:566px;top:1874px"><span></span></div>
  <h2 class="testi-title" style="top:1958px">TESTIMONIALS</h2>
  <svg class="arrow" style="left:116px;top:2098px;height:36px" viewBox="0 0 26 56"><path d="M22 4L4 28l18 24" fill="none" stroke="#fff" stroke-width="4"/></svg>
  <svg class="arrow" style="left:1030px;top:2098px;height:36px" viewBox="0 0 26 56"><path d="M4 4l18 24L4 52" fill="none" stroke="#fff" stroke-width="4"/></svg>

  <blockquote class="testi-card" style="left:175px"><span class="quote-mark">&ldquo;</span><p class="testi-text">Morbi diam mauris viverra in gravida eu mattis in ante Morbi eget arcu Morbi porta libero id ullamcorper nonummy nibh ligula pulvinar metus eget</p></blockquote>
  <blockquote class="testi-card" style="left:465px"><span class="quote-mark">&ldquo;</span><p class="testi-text">Morbi diam mauris viverra in gravida eu mattis in ante Morbi eget arcu Morbi porta libero id ullamcorper nonummy nibh ligula pulvinar metus eget</p></blockquote>
  <blockquote class="testi-card" style="left:755px"><span class="quote-mark">&ldquo;</span><p class="testi-text">Morbi diam mauris viverra in gravida eu mattis in ante Morbi eget arcu Morbi porta libero id ullamcorper nonummy nibh ligula pulvinar metus eget</p></blockquote>

  <div class="author" style="left:182px"><div class="author-photo" role="img" aria-label="Author portrait"></div><div><div class="author-name">By Author Name</div><div class="author-loc">City Location</div></div></div>
  <div class="author" style="left:472px"><div class="author-photo" role="img" aria-label="Author portrait"></div><div><div class="author-name">By Author Name</div><div class="author-loc">City Location</div></div></div>
  <div class="author" style="left:762px"><div class="author-photo" role="img" aria-label="Author portrait"></div><div><div class="author-name">By Author Name</div><div class="author-loc">City Location</div></div></div>

  <!-- team -->
  <h2 class="team-title">OUR TEAM</h2>
  <svg class="arrow" style="left:140px;top:2548px;height:40px" viewBox="0 0 26 56"><path d="M22 4L4 28l18 24" fill="none" stroke="#888" stroke-width="3"/></svg>
  <svg class="arrow" style="left:1024px;top:2548px;height:40px" viewBox="0 0 26 56"><path d="M4 4l18 24L4 52" fill="none" stroke="#888" stroke-width="3"/></svg>

  <article class="team-card" style="left:190px"><div class="team-photo" role="img" aria-label="Team member portrait"></div><h3 class="member-name">Member Name</h3><p class="member-bio">Excepteur sint occaecat cupidatat non proident, sunt in culpa qui officia deserunt</p><div class="member-social"><i></i><i></i><i></i><i></i><i></i></div><div class="btn-red">READ MORE</div></article>
  <article class="team-card" style="left:397px"><div class="team-photo" role="img" aria-label="Team member portrait"></div><h3 class="member-name">Member Name</h3><p class="member-bio">Excepteur sint occaecat cupidatat non proident, sunt in culpa qui officia deserunt</p><div class="member-social"><i></i><i></i><i></i><i></i><i></i></div><div class="btn-red">READ MORE</div></article>
  <article class="team-card" style="left:601px"><div class="team-photo" role="img" aria-label="Team member portrait"></div><h3 class="member-name">Member Name</h3><p class="member-bio">Excepteur sint occaecat cupidatat non proident, sunt in culpa qui officia deserunt</p><div class="member-social"><i></i><i></i><i></i><i></i><i></i></div><div class="btn-red">READ MORE</div></article>
  <article class="team-card" style="left:808px"><div class="team-photo" role="img" aria-label="Team member portrait"></div><h3 class="member-name">Member Name</h3><p class="member-bio">Excepteur sint occaecat cupidatat non proident, sunt in culpa qui officia deserunt</p><div class="member-social"><i></i><i></i><i></i><i></i><i></i></div><div class="btn-red">READ MORE</div></article>

  <!-- fun facts -->
  <svg class="abs" style="left:0;top:2790px" width="1200" height="480" viewBox="0 0 1200 480" preserveAspectRatio="none">
    <defs><linearGradient id="factsGreen" x1="0" y1="0" x2="0" y2="1"><stop offset="0" stop-color="#8fcc44"/><stop offset="1" stop-color="#4ea51e"/></linearGradient></defs>
    <path d="M0 50 Q600 -20 1200 50 L1200 480 L0 480 Z" fill="url(#factsGreen)"/>
  </svg>
  <div class="section-badge" style="left:572px;top:2796px;width:56px;height:56px"><span></span></div>
  <h2 class="facts-title">FUN FACTS</h2>
  <div class="fact" style="top:2970px"><span class="fact-icon"></span><p>Aetus vitae adipiscing semper mauris ipsum iaculis elit congue gravida elit mi egestas orci Curabitur pede</p></div>
  <div class="fact" style="top:3031px"><span class="fact-icon"></span><p>Maecenas aliquet velit vel turpis Mauris neque metus malesuada nec ultricies sit amet porttitor mattis enim</p></div>
  <div class="fact" style="top:3092px"><span class="fact-icon"></span><p>In massa libero interdum nec interdum vel blandit sed nulla In ullamcorper est eget tempor cursus neque mi</p></div>
  <div class="basket-img" role="img" aria-label="Wicker basket full of red apples"></div>

  <!-- footer -->
  <svg class="abs" style="left:0;top:3225px" width="1200" height="353" viewBox="0 0 1200 353" preserveAspectRatio="none">
    <path d="M0 40 Q600 -20 1200 40 L1200 353 L0 353 Z" fill="var(--dark)"/>
  </svg>
  <div class="footer-logo"><div class="mark"></div><div class="name">HARVEST LANE</div></div>

  <div class="foot-col" style="left:406px"><h4>QUICK LINKS</h4><ul><li>About Us</li><li>Our Services</li><li>Products</li><li>Testimonials</li></ul></div>
  <div class="foot-col" style="left:587px"><h4>RESOURCES</h4><ul><li>Support</li><li>Blogs</li><li>Fun Facts</li><li>Contact Us</li></ul></div>
  <div class="foot-col" style="left:757px">
    <h4>CONTACT US</h4>
    <div class="contact-row"><svg width="12" height="16" viewBox="0 0 12 16"><path d="M6 0a6 6 0 0 1 6 6c0 4-6 10-6 10S0 10 0 6a6 6 0 0 1 6-6z" fill="#ddd"/><circle cx="6" cy="6" r="2.2" fill="#262626"/></svg>48 Orchard Row, Suite 3, Austin TX 73301</div>
    <div class="contact-row"><svg width="14" height="14" viewBox="0 0 14 14"><path d="M3 1l2 3-1.5 1.5a8 8 0 0 0 5 5L10 9l3 2-1.5 2.5C6 13 1 8 .5 2.5z" fill="none" stroke="#ddd" stroke-width="1.2"/></svg>555.014.2290</div>
    <div class="contact-row"><svg width="14" height="11" viewBox="0 0 14 11"><rect x=".6" y=".6" width="12.8" height="9.8" fill="none" stroke="#ddd" stroke-width="1.2"/><path d="M1 1l6 5 6-5" fill="none" stroke="#ddd" stroke-width="1.2"/></svg>hello@harvestlane.example</div>
    <div class="social"><i></i><i></i><i></i><i></i><i></i></div>
  </div>

  <div class="copyright">© 2018 Company Name &nbsp;All right reserved &nbsp;Term of Use</div>
</div>
</body>
</html>
```